BRIM Outreach Partners Business Card Rebrand

Hello Designers! We are looking for help designing our new business card to go in conjunction with our company rebrand. Unfortunately, we have an event mid June that requires we get these printed ASAP (before our new website is launched.) We have a mostly complete Brand Book which I have uploaded to this request for your reference to company information, style, fonts. I've also enclosed our logo file in .eps & .jpg. Attached is a sample business card my boss liked but said was "too simple." I made it in Canva and do not profess to be a designer. NOT FOR DESIGN REFERENCE, ONLY FOR CONTEXT Here is what our old website looks like: https://brimoutreachpartners.com/.

```html
<!DOCTYPE html>
<html lang="en">
<head>
<meta charset="utf-8">
<title>BRIM Outreach Partners – Business Card</title>
<link rel="stylesheet" href="https://fonts.googleapis.com/css2?family=Arimo:wght@400;700&display=swap">
<style>
  :root {
    --brand-blue: #4fb3e6;
    --ink: #111111;
    --paper: #ffffff;
    --backdrop: #e6e6e4;
    --card-w: 560px;
    --card-h: 320px;
  }
  * { box-sizing: border-box; margin: 0; padding: 0; }
  html, body {
    width: 1200px;
    height: 900px;
    overflow: hidden;
    background: var(--backdrop);
    font-family: "Arimo", Arial, sans-serif;
    color: var(--ink);
  }
  .canvas { position: relative; width: 1200px; height: 900px; }

  .card {
    position: absolute;
    width: var(--card-w);
    height: var(--card-h);
    background: var(--paper);
    box-shadow: 0 10px 30px rgba(0,0,0,0.18);
    overflow: hidden;
  }
  .card--front { left: 60px; top: 110px; }
  .card--back  { left: 580px; top: 470px; }

  /* Front */
  .brand {
    position: absolute;
    left: 0; right: 0; top: 96px;
    display: flex;
    align-items: center;
    justify-content: center;
    gap: 16px;
  }
  .brand__dot {
    width: 58px; height: 58px;
    border-radius: 50%;
    background: var(--brand-blue);
    flex: none;
  }
  .brand__name {
    font-size: 34px;
    font-weight: 700;
    line-height: 1.05;
    color: var(--ink);
    letter-spacing: 0.5px;
  }
  .front__tagline {
    position: absolute;
    left: 0; right: 0; bottom: 58px;
    text-align: center;
    font-size: 15px;
    letter-spacing: 0.4px;
  }

  /* Back */
  .person {
    position: absolute;
    left: 42px; top: 52px;
    width: 250px;
    padding-bottom: 12px;
    border-bottom: 1.5px solid var(--brand-blue);
  }
  .person__name {
    font-size: 27px;
    color: var(--brand-blue);
    letter-spacing: 0.3px;
  }
  .person__role {
    font-size: 15px;
    font-weight: 700;
    margin-top: 2px;
  }
  .contact {
    position: absolute;
    left: 42px; top: 186px;
    list-style: none;
    font-size: 14px;
    line-height: 22px;
  }
  .contact__item { display: flex; align-items: center; gap: 8px; }
  .contact__icon { width: 13px; height: 13px; flex: none; }
  .back__graphic { position: absolute; inset: 0; }
</style>
</head>
<body>
<main class="canvas">

  <section class="card card--front" aria-label="Business card front">
    <div class="brand">
      <span class="brand__dot" aria-hidden="true"></span>
      <span class="brand__name">BRIM Outreach<br>Partners</span>
    </div>
    <p class="front__tagline">Dayton, OH Based (Eastern Time)</p>
  </section>

  <section class="card card--back" aria-label="Business card back">
    <svg class="back__graphic" viewBox="0 0 560 320" width="560" height="320" aria-hidden="true">
      <rect class="band band--ink" x="0" y="298" width="360" height="22" fill="var(--ink)"/>
      <polygon class="band band--blue" points="338,320 372,214 560,138 560,320" fill="var(--brand-blue)"/>
    </svg>

    <div class="person">
      <h1 class="person__name">Daniel Harrow-Lane</h1>
      <p class="person__role">Inhaber</p>
    </div>

    <ul class="contact">
      <li class="contact__item">
        <svg class="contact__icon" viewBox="0 0 16 16" aria-hidden="true"><path fill="var(--brand-blue)" d="M3.6 1.5l2.3 2.6-1.3 1.8c.9 2 2.5 3.6 4.5 4.5l1.8-1.3 2.6 2.3-1.4 2.3C7 13.6 2.4 9 1.3 3z"/></svg>
        +945-555-0142
      </li>
      <li class="contact__item">
        <svg class="contact__icon" viewBox="0 0 16 16" aria-hidden="true"><rect x="1" y="3" width="14" height="10" fill="var(--brand-blue)"/><path d="M1 3l7 6 7-6" fill="none" stroke="#fff" stroke-width="1.2"/></svg>
        daniel@brimoutreachpartners.com
      </li>
      <li class="contact__item">
        <svg class="contact__icon" viewBox="0 0 16 16" aria-hidden="true"><circle cx="8" cy="8" r="7" fill="var(--brand-blue)"/><path d="M1 8h14M8 1c-3 3-3 11 0 14M8 1c3 3 3 11 0 14" fill="none" stroke="#fff" stroke-width="1"/></svg>
        www.brimoutreachpartners.com
      </li>
    </ul>
  </section>

</main>
</body>
</html>
```